Women's Empowerment & Prayer Brunch - Matching Poster, flyer and Postcard

We are a Christian Event & Travel Company and we are hosting our inaugural event on June 10, 2017. This event is a women's empowerment & prayer brunch aboard a private yacht leaving out of Larkspur Landing, Maryland. The event will cater to women who have a vision to start or have already embarked on the journey of starting or growing a business or ministry. The event calls for a matching poster, flyer and postcard design that give an elegant & exquisite feel with just the right breath of freshness. The colors should reflect our logo as this is our launch event. I have also included 2 photos of the Coralwind Heritage Village production (one of our sponsors) - Please include but do not make it take over the design - this is to advertise the door prize. The final design will portray the branding of the company (Christian, travel, events, elegance, professional), the branding of the event (elegant and luxurious) and the importance of this launch event.
Please include the following information:
Brightwell Event & Travel Group presents
Event name: Climbing the Hill: Trust, Service & Devotion.
Tag Line/Description: An Exquisite Women's Empowerment & Prayer Brunch.
Guest Speaker: Minister Harriet L. Dunmore (Photo included)
VP of TrustLine
Asst. Pastor & First Lady of Gilead Baptist Church
Special Guest Psalmist: Minister Tessa Holbrook (Photo Included)
Worship Director of Stonefield Community Church
Vocalist, Songwriter, Musician, and Clinician
Venue: Aboard the Regal Tide Yacht
Dock: Larkspur Landing
342 Marlow Court, Oxen Hill, MD 20712
Boarding 10:00am
Sailing Promptly at 10:30am
(Please be on time the yacht will not wait)
Date: Saturday June 10, 2017
Tickets: Early Bird US$75.00/person (ends May 15, 2017)
Regular Tickets US$95.99
Purchase Tickets at www.brightwellevent-travel.example/climbing-the-hill
SPACE IS LIMITED DUE TO YACHT CAPACITY
Grand Prize: Julian Ardent Purse
Door Prize: 2 Tickets to the Islander Coralwind Heritage Village
Other prizes for special ladies in attendance.
Ladies are asked to dress in Elegant White Ensemble
Corporate Sponsors:
The Coralwind Heritage Village (Logo included)
R. Lanning Photography (Logo included)
Special Thanks to our Individual Sponsors:
Mrs. G. Whitlow, Mr. K Prentice & Mr. S. Dorsey

Target Market(s)

Women, Business, Ministry, Christians, Middle to Upper Class

Industry/Entity Type

Events

Font styles to use
Serif
Script

Requirements
Must have
• Elegance, professional, vivid in color & font. be creative in Visual and FONT!
• Poster: 18" X 24"
• Flyer: one sided.
• ***** the final design chosen will have a cross referenced design of 1 flyer, 1 postcard 1 poster. This was included so you have a reference - Be creative!!!!!!
Nice to have
• Matching across all 3 designs (poster, flyer & postcard) but sized appropriately and just enough difference to play up the design and be appealing.
• I uploaded 3 example flyers to give you inspiration of the type of visuals I'm looking for. I removed my amateur sample because the designs were copying it instead of being creative.
Should not have
• Any thing inappropriate, alcohol oriented or sexual

```html
<!DOCTYPE html>
<html lang="en">
<head>
<meta charset="utf-8">
<title>Climbing the Hill – Women's Empowerment &amp; Prayer Brunch</title>
<link href="https://fonts.googleapis.com/css2?family=Cinzel:wght@400;700&family=Playfair+Display:ital,wght@0,400;0,700;1,400;1,700&family=Great+Vibes&family=Lato:wght@400;700;900&display=swap" rel="stylesheet">
<style>
  :root{
    --ink:#0b0710;
    --plum:#4a1460;
    --violet:#6b2a86;
    --lavender:#d9c4ea;
    --gold:#e0b24f;
    --gold-light:#f6dc8e;
    --white:#ffffff;
    --paper:#ffffff;
    --text-dark:#1d1424;
    --muted:#555555;
  }
  *{margin:0;padding:0;box-sizing:border-box}
  html,body{width:900px;height:1200px;overflow:hidden;background:var(--paper)}
  .poster{position:relative;width:900px;height:1200px;overflow:hidden;font-family:'Lato',sans-serif;background:var(--paper)}

  .hero{position:absolute;left:0;top:0;width:900px;height:990px;background:linear-gradient(180deg,#120a18 0%,#0b0710 48%,#2b0c3a 66%,var(--plum) 100%)}
  .speaker-photos{position:absolute;left:0;top:0;width:430px;height:320px;background:radial-gradient(ellipse at 60% 45%,#7a2a2e 0%,#3a1b24 45%,#120a18 80%)}
  .brand-mark{position:absolute;left:590px;top:28px;width:200px;height:130px;background:#151a3a;border-radius:6px;display:flex;align-items:center;justify-content:center;gap:10px}
  .brand-mark .dot{width:14px;height:14px;border-radius:50%;background:var(--gold);flex:none}
  .brand-mark span{font-family:'Playfair Display',serif;font-size:19px;color:var(--gold);text-align:center;line-height:1.2}

  .title{position:absolute;left:0;width:900px;top:325px;text-align:center;font-family:'Cinzel',serif;font-weight:700;font-size:68px;letter-spacing:2px;line-height:1.1;
    background:linear-gradient(180deg,var(--gold-light) 0%,var(--gold) 55%,#a8741f 100%);-webkit-background-clip:text;background-clip:text;color:transparent}
  .subtitle{position:absolute;left:0;width:900px;top:412px;text-align:center;font-family:'Playfair Display',serif;font-style:italic;font-size:32px;color:var(--white)}
  .tagline{position:absolute;left:0;width:900px;top:458px;text-align:center;font-family:'Playfair Display',serif;font-style:italic;font-size:22px;color:var(--white)}

  .fire-photo{position:absolute;left:450px;top:505px;width:450px;height:290px;background:radial-gradient(ellipse at 50% 40%,#f0a03a 0%,#b0451c 25%,#3c1530 60%,#1a0d20 100%)}

  .guests{position:absolute;left:30px;top:510px;width:410px;color:var(--white)}
  .guests .label{font-family:'Playfair Display',serif;font-size:16px;color:var(--lavender)}
  .guests .name{font-family:'Playfair Display',serif;font-size:19px;color:var(--white)}
  .guests .role{font-size:12px;color:var(--lavender);line-height:1.35;margin-top:2px}
  .guests .gap{height:10px}

  .venue{position:absolute;left:30px;top:690px;width:410px;text-align:center;color:var(--white);font-size:13px;line-height:1.5}
  .venue b{font-weight:700;font-size:14px}
  .venue small{font-size:12px}

  .date{position:absolute;left:30px;top:805px;width:540px;font-family:'Cinzel',serif;font-weight:700;font-size:32px;color:var(--white);white-space:nowrap}
  .tickets{position:absolute;left:30px;top:860px;width:540px;color:var(--white);font-size:14px;line-height:1.45}
  .tickets b{font-weight:900}

  .dance-photo{position:absolute;left:580px;top:810px;width:320px;height:220px;background:linear-gradient(180deg,#3b5a3a 0%,#7a5a2e 55%,#b6532b 100%)}

  .prizes{position:absolute;left:30px;top:1005px;width:560px;color:var(--text-dark)}
  .limited{font-weight:900;font-size:21px;color:var(--plum);letter-spacing:.5px}
  .prize-row{display:flex;align-items:center;margin-top:9px;font-size:15px}
  .prize-row .tag{background:var(--plum);color:var(--white);font-weight:700;padding:5px 12px;width:120px;margin-right:12px;flex:none}
  .prize-row .value{font-weight:700}
  .other{margin-top:10px;font-size:15px;color:var(--muted)}
  .dress{font-size:15px;color:var(--muted)}
  .dress em{font-family:'Great Vibes',cursive;font-style:normal;font-size:26px;color:var(--plum)}

  .sponsors-label{position:absolute;left:600px;width:280px;text-align:right;top:1042px;font-size:12px;font-weight:700;color:var(--text-dark)}
  .sponsor{position:absolute;display:flex;align-items:center;gap:8px;font-size:13px;font-weight:700;color:var(--text-dark);line-height:1.25}
  .sponsor .dot{width:34px;height:34px;border-radius:50%;background:var(--violet);flex:none}
  .sponsor.one{left:605px;top:1064px;width:135px}
  .sponsor.two{left:745px;top:1064px;width:150px}
  .thanks{position:absolute;left:690px;top:1120px;width:200px;font-size:11px;line-height:1.4;color:var(--text-dark);font-weight:700}
</style>
</head>
<body>
<main class="poster">
  <section class="hero">
    <div class="speaker-photos" role="img" aria-label="Portraits of the guest speaker and the special guest psalmist"></div>
    <div class="brand-mark"><i class="dot"></i><span>Brightwell Event<br>&amp; Travel Group</span></div>

    <h1 class="title">CLIMBING THE HILL</h1>
    <p class="subtitle">Trust, Service &amp; Devotion</p>
    <p class="tagline">An Exquisite Women's Empowerment &amp; Prayer Brunch.</p>

    <div class="fire-photo" role="img" aria-label="Fire dancers performing at night at the heritage village"></div>

    <div class="guests">
      <p><span class="label">Guest Speaker: </span><span class="name">Minister Harriet L. Dunmore</span></p>
      <p class="role">VP of TrustLine, Asst. Pastor &amp; First Lady of Gilead Baptist Church</p>
      <div class="gap"></div>
      <p><span class="label">Special Guest Psalmist: </span><span class="name">Minister Tessa Holbrook</span></p>
      <p class="role">Worship Director of Stonefield Community Church Vocalist,<br>Songwriter, Musician, and Clinician</p>
    </div>

    <div class="venue">
      <p>Venue: Aboard the Regal Tide Yacht</p>
      <p>Dock: Larkspur Landing, 342 Marlow Court, Oxen Hill, MD 20712</p>
      <p><b>Boarding 10:00am | Sailing Promptly at 10:30am</b></p>
      <p><small>(Please be on time the yacht will not wait)</small></p>
    </div>

    <p class="date">SATURDAY JUNE 10, 2017</p>
    <div class="tickets">
      <p><b>Tickets</b> Early Bird US$75.00/person (ends May 15, 2017)</p>
      <p>Regular Tickets US$95.99</p>
      <p>Purchase Tickets at www.brightwellevent-travel.example/climbing-the-hill</p>
    </div>
  </section>

  <div class="dance-photo" role="img" aria-label="Island dancers in traditional costume on stage"></div>

  <section class="prizes">
    <p class="limited">SPACE IS LIMITED DUE TO YACHT CAPACITY</p>
    <div class="prize-row"><span class="tag">Grand Prize</span><span class="value">Julian Ardent Purse</span></div>
    <div class="prize-row"><span class="tag">Door Prize</span><span class="value">2 Tickets to the Islander Coralwind Heritage Village</span></div>
    <p class="other">Other prizes for special ladies in attendance.</p>
    <p class="dress">Ladies are asked to dress in <em>Elegant White Ensemble</em></p>
  </section>

  <p class="sponsors-label">Corporate Sponsors:</p>
  <div class="sponsor one"><i class="dot"></i><span>R. Lanning Photography</span></div>
  <div class="sponsor two"><i class="dot"></i><span>Coralwind Heritage Village</span></div>
  <p class="thanks">Special Thanks to our Individual Sponsors:<br>Mrs. G. Whitlow, Mr. K Prentice &amp; Mr. S. Dorsey</p>
</main>
</body>
</html>
```